Like us

We need a contest ad that offers a free weekend getaway stay in our Spa Suite- Bridal or Family Suite or King Suite, winners choice. (subject to availability, some conditions apply)
Objective - to encourage existing followers to refer friends and obtain new likes. Each referral "like" should leave a comment with just the referral name in the comment line. We will compile these referral names and the new like names for 1 "referer" weekend getaway package & 1 new "like" weekend getaway package Prize package includes a dinner certificate at the Marlow Hearth (value $ 30) & a complimentary bottle of champagne
(In room or at the Restaurant.) Facebook Contest closes June 30th, 2014. The professional image is the important part of the design, comment lines can be used for contest explanations, however it would be nice to incorporate in the design. Design first!
The Motel Logo is AR Bonnie with a shadow. (bad copy uploaded)

Target Market(s)

Travelers

Industry/Entity Type

Restaurant

Requirements
Must have
• Professional Image
Nice to have
• Explanation of contest

```html
<!DOCTYPE html>
<html lang="en">
<head>
<meta charset="utf-8">
<title>Win a Spa Suite Getaway</title>
<link rel="stylesheet" href="https://fonts.googleapis.com/css2?family=Raleway:wght@800;900&family=Great+Vibes&family=Arimo&display=swap">
<style>
  :root {
    --text-white: #ffffff;
    --sky-blue: #5d7fa6;
    --cloud-grey: #c9ced3;
    --palm-green: #2f4a33;
    --palm-dark: #1c2a22;
    --trunk-brown: #4a3a2c;
  }
  html, body {
    margin: 0;
    padding: 0;
    overflow: hidden;
    background: #ffffff;
  }
  .contest-ad {
    position: relative;
    width: 1200px;
    height: 628px;
    overflow: hidden;
    color: var(--text-white);
  }
  .palm-sky-photo {
    position: absolute;
    inset: 0;
    background:
      radial-gradient(ellipse 420px 320px at 20% 25%, rgba(47,74,51,0.85), transparent 70%),
      radial-gradient(ellipse 380px 260px at 85% 18%, rgba(28,42,34,0.8), transparent 70%),
      radial-gradient(ellipse 360px 220px at 88% 78%, rgba(47,74,51,0.75), transparent 70%),
      radial-gradient(ellipse 300px 200px at 8% 85%, rgba(74,58,44,0.6), transparent 70%),
      radial-gradient(ellipse 500px 300px at 55% 45%, rgba(201,206,211,0.7), transparent 75%),
      linear-gradient(160deg, var(--sky-blue) 0%, #8a9cae 45%, #7f8f9b 100%);
  }
  .headline {
    position: absolute;
    left: 0;
    width: 100%;
    top: 196px;
    margin: 0;
    text-align: center;
    font-family: "Raleway", sans-serif;
    font-weight: 900;
    font-size: 113px;
    line-height: 1;
    letter-spacing: 1px;
  }
  .divider {
    position: absolute;
    top: 356px;
    height: 12px;
    background: var(--text-white);
  }
  .divider--left { left: 157px; width: 231px; }
  .divider--right { left: 806px; width: 234px; }
  .subhead {
    position: absolute;
    left: 0;
    width: 100%;
    top: 312px;
    margin: 0;
    text-align: center;
    font-family: "Great Vibes", cursive;
    font-weight: 400;
    font-size: 100px;
    line-height: 1;
    padding-left: 10px;
  }
  .instructions {
    position: absolute;
    left: 0;
    width: 100%;
    top: 423px;
    margin: 0;
    text-align: center;
    font-family: "Raleway", sans-serif;
    font-weight: 800;
    font-size: 31px;
    line-height: 47px;
  }
  .fine-print {
    position: absolute;
    left: 0;
    width: 100%;
    top: 571px;
    margin: 0;
    text-align: center;
    font-family: "Arimo", sans-serif;
    font-size: 16.5px;
    line-height: 27px;
  }
</style>
</head>
<body>
  <main class="contest-ad">
    <div class="palm-sky-photo" role="img" aria-label="Looking up at tall palm trees against a blue sky with soft white clouds"></div>

    <h1 class="headline">WIN A SPA SUITE</h1>
    <span class="divider divider--left"></span>
    <span class="divider divider--right"></span>
    <p class="subhead">Getaway</p>

    <p class="instructions">Just refer our page to a friend and have them like it, as<br>well write a comment mentioning your name.</p>

    <p class="fine-print">Prize package includes a dinner certificate at the Marlow Hearth (value $ 30) &amp; a complimentary bottle of champagne.<br>(subject to availability, some conditions apply)</p>
  </main>
</body>
</html>
```